NYC and MIAMI Trendy Womans Boutique Custom Mailing Packaging

Im looking for help designing custom mailing pouches for my woman's retail store. Weve been doing a lot of online sales lately and Its time to upgrade to custom packaging. I want it to look fun and playful but not too childish or cheesy.
Please see our website www.tavorila.com and our instagram account @tavorila to get a feel for our brand.

Target Market(s)

From teens- 60 year old

Industry/Entity Type

Clothing Brand

Colors
feeeee
fff9f9
fdf3f8

Requirements
Must have
• Pink :) I need it to be girly, fun, but also classy and sophisticated
Should not have
• Look childish or cheesy

```html
<!DOCTYPE html>
<html lang="en">
<head>
<meta charset="utf-8">
<title>Tavorila – Mailing Pouch Designs</title>
<link rel="stylesheet" href="https://fonts.googleapis.com/css2?family=Quicksand:wght@400;500&display=swap">
<style>
  :root {
    --backdrop-light: #f4f4f5;
    --backdrop-dark: #bcbdbf;
    --paper: #ffffff;
    --pattern-tint: #f3f3f3;
    --brand-pink: #f094b0;
    --brand-pink-deep: #d9809a;
    --lace-pink: #f7b9cb;
    --ink-light: #ffffff;
  }
  html, body {
    margin: 0;
    padding: 0;
    width: 1200px;
    height: 1000px;
    overflow: hidden;
  }
  body {
    position: relative;
    background: radial-gradient(ellipse 55% 60% at 50% 50%, var(--backdrop-light) 0%, var(--backdrop-dark) 100%);
    font-family: "Quicksand", sans-serif;
  }
  .pouch {
    position: absolute;
    top: 174px;
    width: 440px;
    height: 628px;
  }
  .pouch--front { left: 135px; }
  .pouch--back { left: 687px; }

  .front-face {
    position: absolute;
    inset: 0 0 55px 0;
    background: linear-gradient(180deg, var(--paper) 0%, var(--pattern-tint) 100%);
  }
  .front-flap {
    position: absolute;
    left: 1px;
    right: 1px;
    bottom: 0;
    height: 55px;
    background: var(--brand-pink);
    border-top: 3px solid var(--brand-pink-deep);
    box-sizing: border-box;
  }
  .brand-badge {
    position: absolute;
    left: 36px;
    top: 54px;
    width: 158px;
    height: 158px;
    border-radius: 50%;
    background: var(--brand-pink);
    display: flex;
    align-items: center;
    justify-content: center;
  }
  .brand-name {
    color: var(--ink-light);
    font-weight: 500;
    font-size: 24px;
    letter-spacing: 3px;
  }
  .site-url {
    position: absolute;
    right: 7px;
    bottom: 64px;
    font-size: 10px;
    letter-spacing: 1px;
    color: var(--brand-pink);
  }

  .back-face {
    position: absolute;
    inset: 0;
    background: var(--brand-pink);
    overflow: hidden;
  }
  .back-art {
    position: absolute;
    inset: 0;
  }
  .back-art text {
    font-family: "Quicksand", sans-serif;
    font-weight: 500;
    font-size: 24px;
    letter-spacing: 3px;
    fill: var(--ink-light);
  }
</style>
</head>
<body>
  <section class="pouch pouch--front" aria-label="Front of mailing pouch">
    <div class="front-face" role="img" aria-label="Faint white-on-white floral swirl pattern covering the pouch front"></div>
    <div class="brand-badge"><span class="brand-name">TAVORILA</span></div>
    <span class="site-url">www.tavorila.com</span>
    <div class="front-flap"></div>
  </section>

  <section class="pouch pouch--back" aria-label="Back of mailing pouch">
    <div class="back-face">
      <svg class="back-art" width="440" height="628" viewBox="0 0 440 628">
        <defs>
          <radialGradient id="lace-glow" cx="50%" cy="50%" r="50%">
            <stop offset="0%" stop-color="#f6b0c4"/>
            <stop offset="70%" stop-color="#f5aac0"/>
            <stop offset="100%" stop-color="#f29cb6"/>
          </radialGradient>
        </defs>
        <circle cx="113" cy="135" r="251" fill="url(#lace-glow)" role="img" aria-label="Large white lace mandala ornament radiating from the upper left corner"/>
        <circle cx="113" cy="135" r="89" fill="var(--brand-pink)"/>
        <text x="113" y="143" text-anchor="middle">TAVORILA</text>
      </svg>
    </div>
  </section>
</body>
</html>
```